Dorsey K. Wendell Business Card

We need a business card for our company Dorsey K. Wendell Heating & Plumbing to be distributed to potential customers. It should follow the color scheme of our logo and have a modern upscale and masculine look.

The logo is attached and the info below should also be included:

5187 W. Cedar Brook Rd.
Ridgeford, PA 17632

Russell T. Wendell
(717) 592-0817
russelltwendell@fernmail.net
dorseykwendell.net
PA #093148

Industry/Entity Type

Business

Contact Information for Business Card

5187 W. Cedar Brook Rd.
Ridgeford, PA 17632

Russell T. Wendell
(717) 592-0817
russelltwendell@fernmail.net
dorseykwendell.net
PA #093148

Colors

Designer to choose colors to be used in the design.

Requirements
Must have
• Information above included

```html
<!DOCTYPE html>
<html lang="en">
<head>
<meta charset="utf-8">
<title>Dorsey K. Wendell Business Card</title>
<link rel="stylesheet" href="https://fonts.googleapis.com/css2?family=Lato:wght@400;700;900&display=swap">
<style>
  :root {
    --page-bg: #e9e9e6;
    --brand-blue: #0b77c5;
    --brand-blue-deep: #0761b0;
    --accent-green: #b5d334;
    --card-white: #f7f7f5;
    --text-blue: #1268b3;
    --text-grey: #3f5f86;
    --icon-green: #b5d334;
  }
  html, body {
    margin: 0;
    padding: 0;
    width: 1200px;
    height: 780px;
    overflow: hidden;
    background: var(--page-bg);
    font-family: "Lato", Arial, sans-serif;
  }
  .sheet {
    position: relative;
    width: 1200px;
    height: 780px;
    display: flex;
    align-items: center;
    justify-content: center;
    gap: 40px;
  }
  .card {
    position: relative;
    width: 560px;
    height: 320px;
    border-radius: 14px;
    overflow: hidden;
    box-shadow: 0 6px 18px rgba(0,0,0,0.18);
  }

  /* Front */
  .card-front { background: var(--card-white); }
  .front-band {
    position: absolute;
    left: 0; top: 0;
    width: 372px; height: 134px;
    background: linear-gradient(90deg, var(--brand-blue-deep), var(--brand-blue));
  }
  .front-rule {
    position: absolute;
    left: 0; top: 140px;
    width: 372px; height: 4px;
    background: var(--accent-green);
  }
  .front-block {
    position: absolute;
    left: 382px; top: 0;
    width: 96px; height: 98px;
    background: var(--brand-blue);
  }
  .company-mark {
    position: absolute;
    left: 24px; top: 36px;
    display: flex;
    align-items: center;
    gap: 14px;
  }
  .company-mark .mark-square {
    width: 52px; height: 52px;
    background: #ffffff;
    flex: none;
  }
  .company-mark .mark-name {
    color: #ffffff;
    font-weight: 900;
    font-size: 22px;
    line-height: 1.15;
    text-transform: uppercase;
    letter-spacing: 0.5px;
  }
  .address {
    position: absolute;
    right: 28px; top: 160px;
    text-align: right;
    font-style: normal;
    color: var(--text-blue);
    font-size: 14px;
    line-height: 1.4;
  }
  .person {
    position: absolute;
    left: 30px; top: 172px;
  }
  .person-name {
    color: var(--text-blue);
    font-size: 21px;
    font-weight: 400;
    margin: 0;
  }
  .person-license {
    color: var(--accent-green);
    font-size: 14px;
    margin: 2px 0 0;
  }
  .contacts {
    list-style: none;
    margin: 10px 0 0;
    padding: 0;
  }
  .contacts li {
    display: flex;
    align-items: center;
    gap: 8px;
    color: var(--text-grey);
    font-size: 14px;
    line-height: 1.5;
  }
  .contacts svg { width: 14px; height: 14px; flex: none; }

  /* Back */
  .card-back {
    background: linear-gradient(135deg, #1a7fd0 0%, var(--brand-blue) 50%, var(--brand-blue-deep) 100%);
    display: flex;
    align-items: center;
    justify-content: center;
  }
  .card-back .company-mark { position: static; }
  .card-back .mark-name { font-size: 26px; }
  .card-back .mark-square { width: 60px; height: 60px; }
</style>
</head>
<body>
<main class="sheet">

  <section class="card card-front" aria-label="Card front">
    <div class="front-band"></div>
    <div class="front-rule"></div>
    <div class="front-block"></div>

    <div class="company-mark">
      <span class="mark-square"></span>
      <span class="mark-name">Dorsey K. Wendell<br>Heating &amp; Plumbing</span>
    </div>

    <address class="address">
      5187 W. Cedar Brook Rd.<br>
      Ridgeford, PA 17632
    </address>

    <div class="person">
      <p class="person-name">Russell T. Wendell</p>
      <p class="person-license">PA #093148</p>
      <ul class="contacts">
        <li>
          <svg viewBox="0 0 16 16" aria-hidden="true"><circle cx="8" cy="8" r="7" fill="none" stroke="var(--icon-green)" stroke-width="1.4"/><path d="M5.5 4.5l1.5 0 .6 1.8-1 .8a5 5 0 0 0 2.3 2.3l.8-1 1.8.6v1.5c-3.6.3-6.3-2.4-6-6z" fill="var(--icon-green)"/></svg>
          (717) 592-0817
        </li>
        <li>
          <svg viewBox="0 0 16 16" aria-hidden="true"><circle cx="8" cy="8" r="7" fill="none" stroke="var(--icon-green)" stroke-width="1.4"/><rect x="4.3" y="5.3" width="7.4" height="5.4" fill="none" stroke="var(--icon-green)" stroke-width="1.1"/><path d="M4.3 5.3L8 8.3l3.7-3" fill="none" stroke="var(--icon-green)" stroke-width="1.1"/></svg>
          russelltwendell@fernmail.net
        </li>
        <li>
          <svg viewBox="0 0 16 16" aria-hidden="true"><circle cx="8" cy="8" r="7" fill="none" stroke="var(--icon-green)" stroke-width="1.4"/><circle cx="8" cy="8" r="3.8" fill="none" stroke="var(--icon-green)" stroke-width="1"/><path d="M4.2 8h7.6M8 4.2c-1.6 2.2-1.6 5.4 0 7.6M8 4.2c1.6 2.2 1.6 5.4 0 7.6" fill="none" stroke="var(--icon-green)" stroke-width="0.9"/></svg>
          dorseykwendell.net
        </li>
      </ul>
    </div>
  </section>

  <section class="card card-back" aria-label="Card back">
    <div class="company-mark">
      <span class="mark-square"></span>
      <span class="mark-name">Dorsey K. Wendell<br>Heating &amp; Plumbing</span>
    </div>
  </section>

</main>
</body>
</html>
```